Need Business Card for eLearning Company

Need a business card designed for our company, CareerTrellon.

CareerTrellon has developed a complete 12 lesson eLearning course to teach you the skills you need to present yourself in a job interview. The course uses advanced learning techniques in the multimedia videos, plus contains quizzes and additional exercises to insure you get the course and can walk into any interview with confidence and ease, and get the job.

www.careertrellon.com

Attached is our logo

Industry/Entity Type

Business

```html
<!DOCTYPE html>
<html lang="en">
<head>
<meta charset="utf-8">
<title>CareerTrellon Business Card</title>
<link rel="stylesheet" href="https://fonts.googleapis.com/css2?family=Arimo:wght@400;700&family=Tinos:wght@400;700&display=swap">
<style>
  :root {
    --backdrop: #6c6c6c;
    --card: #ffffff;
    --card-shade: #f1f1f1;
    --plum: #8e1c74;
    --lime: #95b722;
    --ink: #4a4646;
    --on-band: #ffffff;
  }
  * { box-sizing: border-box; margin: 0; padding: 0; }
  html, body {
    width: 1059px; height: 1200px; overflow: hidden;
    background: var(--backdrop);
  }
  .canvas { position: relative; width: 1059px; height: 1200px; }
  .card {
    position: absolute; left: 151px; width: 792px; height: 456px;
    border-radius: 14px; overflow: hidden;
    background: radial-gradient(ellipse at 50% 20%, var(--card) 40%, var(--card-shade) 100%);
    box-shadow: 0 2px 6px rgba(0,0,0,0.25);
  }
  .card--front { top: 107px; }
  .card--back { top: 611px; height: 455px; }
  .band { position: absolute; left: 0; width: 100%; color: var(--on-band);
    font-family: "Arimo", Arial, sans-serif; }
  .band--plum { background: var(--plum); }
  .band--lime { background: var(--lime); }
  .front-band { top: 376px; height: 80px; display: flex; align-items: center;
    justify-content: center; font-size: 28px; }
  .brand { position: absolute; display: flex; align-items: center; gap: 14px;
    font-family: "Tinos", "Times New Roman", serif; font-weight: 400; color: var(--ink); }
  .brand-mark { background: var(--ink); border-radius: 8px; }
  .brand--hero { left: 0; width: 100%; top: 150px; justify-content: center; font-size: 48px; }
  .brand--hero .brand-mark { width: 60px; height: 60px; }
  .brand--lockup { right: 34px; top: 94px; font-size: 38px; }
  .brand--lockup .brand-mark { width: 38px; height: 38px; border-radius: 6px; }
  .holder { position: absolute; left: 48px; top: 72px;
    font-family: "Tinos", "Times New Roman", serif; color: var(--ink); }
  .holder-name { font-size: 36px; line-height: 40px; }
  .holder-title { font-size: 25px; font-weight: 700; line-height: 30px; }
  .address-band { top: 295px; height: 28px; font-size: 24px; line-height: 28px; text-align: center; }
  .contact-band { top: 323px; height: 132px; font-size: 24px; }
  .phones { position: absolute; left: 22px; top: 34px; line-height: 29px; text-align: center; }
  .online { position: absolute; right: 34px; top: 26px; line-height: 33px; text-align: right; }
</style>
</head>
<body>
<main class="canvas">
  <section class="card card--front">
    <div class="brand brand--hero">
      <span class="brand-mark"></span>
      <span class="brand-name">CareerTrellon</span>
    </div>
    <div class="band band--plum front-band">www.careertrellon.com</div>
  </section>

  <section class="card card--back">
    <div class="holder">
      <p class="holder-name">Daniel Harper</p>
      <p class="holder-title">President</p>
    </div>
    <div class="brand brand--lockup">
      <span class="brand-mark"></span>
      <span class="brand-name">CareerTrellon</span>
    </div>
    <div class="band band--lime address-band">2450 Harbor Crest Avenue Suite 310,Tacoma, WA 98402</div>
    <div class="band band--plum contact-band">
      <p class="phones">US:(555) 014-2368 / In<br>ternational:(65) 5550-1842</p>
      <p class="online">support@careertrellon.com<br>www.careertrellon.com</p>
    </div>
  </section>
</main>
</body>
</html>
```